Roll-up-Banner für Schule gesucht
Zielgruppe
Unsere Schule wünscht einen Rollup (880mm Breite x 2200mm Höhe) für die jährliche Lesenacht für Kinder im Alter von 6-12 Jahren. Diese wären die Produktdaten: https://unterlagen.plavix-laden.de/tb-07-31-stand-banner-simpel-31-infoblatt-datasheet.pdf
Der Rollup sollte für Kinder kreiert werden aber nicht zu kindlich sein.
Aufgabenstellung
Das Logo der Schule müsste ersichtlich sein ansonsten ist Kreativität gefragt ;-)

```html
<!DOCTYPE html>
<html lang="de">
<head>
<meta charset="utf-8">
<title>Lesenacht – Roll-up</title>
<link rel="stylesheet" href="https://fonts.googleapis.com/css2?family=Caveat:wght@600&family=Fira+Sans+Condensed:wght@500&family=Montserrat:wght@700&display=swap">
<style>
  :root {
    --page: #eef0f2;
    --night: #66519a;
    --paper: #ffffff;
    --ink: #ffffff;
    --school: #1f8a3a;
    --art-top: #7d69b0;
    --art-mid: #d9c9d6;
    --art-low: #c9864d;
  }
  * { box-sizing: border-box; margin: 0; padding: 0; }
  html, body { width: 1200px; height: 1200px; overflow: hidden; }
  body { background: var(--page); position: relative; }

  .rollup {
    position: absolute;
    left: 372px; top: 30px;
    width: 456px; height: 1140px;
    background: var(--night);
    overflow: hidden;
  }
  .event-date {
    position: absolute;
    left: 26px; top: 38px;
    font-family: "Fira Sans Condensed", sans-serif;
    font-weight: 500;
    font-size: 70px;
    line-height: 1;
    color: var(--ink);
    letter-spacing: 1px;
    white-space: nowrap;
  }
  .event-title {
    position: absolute;
    left: -330px; top: 470px;
    width: 820px; height: 170px;
    font-family: "Caveat", cursive;
    font-weight: 600;
    font-size: 190px;
    line-height: 170px;
    color: var(--ink);
    text-align: center;
    white-space: nowrap;
    transform: rotate(-90deg);
    transform-origin: center;
  }
  .hero-illustration {
    position: absolute;
    left: 190px; top: 14px;
    width: 260px; height: 962px;
    border-radius: 8px;
    background: linear-gradient(180deg, var(--art-top) 0%, var(--art-mid) 35%, var(--art-mid) 62%, var(--art-low) 80%, #8a9c4a 100%);
    opacity: .8;
  }
  .school-band {
    position: absolute;
    left: 0; bottom: 0;
    width: 100%; height: 158px;
    background: var(--paper);
    display: flex;
    align-items: center;
    justify-content: center;
    gap: 14px;
  }
  .school-mark {
    width: 22px; height: 22px;
    border-radius: 50%;
    background: var(--school);
  }
  .school-name {
    font-family: "Montserrat", sans-serif;
    font-weight: 700;
    font-size: 27px;
    letter-spacing: 4px;
    color: var(--school);
    white-space: nowrap;
  }
</style>
</head>
<body>
  <main class="rollup">
    <div class="hero-illustration" role="img" aria-label="Illustration: Mädchen mit Krone im gepunkteten Schlafanzug steht auf einem bunten Bücherstapel, darüber hängende Sterne"></div>
    <div class="event-date">15.12.</div>
    <h1 class="event-title">Lesenacht</h1>
    <footer class="school-band">
      <span class="school-mark"></span>
      <span class="school-name">SCHULE ERLENHOF</span>
    </footer>
  </main>
</body>
</html>
```